Web Site Redesign

We operate a data centre facility specialing in colocation and Fibre optic connectivity (i.e. point to point fibre services and internet over fibre).

We have an existing site located at www.norvalex.example however this is very very tired and requires a redesign. We are looking for a fresh new design that will be appealing to potential customers.

The Company name is Norva eX and the primary corporate colour is bright red with secondary colours of white, grey and black. Specific bright red can be seen in attached company logo.

Website needs to be modern, clean and professional representing our premium colocation and fibre provider branding.

Our company slogan is : safe. secure. reliable

We will provide feedback regardless of the quality of the design to ensure a better outcome for all parties.

Please feel free to contact us if you have any questions.

# The designer can use placeholder images or feel free to use any/all or none of the attached images
# The designer can use sample filler text

Target Market(s)

Technical IT Professionals as well C level executives (i.e. CEO's, CIO).

Industry/Entity Type

Internet

Requirements
Must have
• clean design
Nice to have
• A sidebar with two sections. 1 for current promo and 1 for "Let us call you back/contact you"
Should not have
• Clutter

```html
<!DOCTYPE html>
<html lang="en">
<head>
<meta charset="utf-8">
<title>Norva eX — Safe, Secure, Reliable Data Centre</title>
<link href="https://fonts.googleapis.com/css2?family=Noto+Serif:wght@400;700&display=swap" rel="stylesheet">
<style>
:root{
  --red:#d3262a;
  --red-dark:#a80f12;
  --ink:#1e1e1e;
  --charcoal:#262626;
  --text:#333;
  --line:#d8d8d8;
  --white:#fff;
}
*{margin:0;padding:0;box-sizing:border-box}
html,body{width:1192px;height:1200px;overflow:hidden;background:var(--white)}
body{font-family:"Noto Serif",Georgia,serif;color:var(--text)}
.stage{position:absolute;left:0;top:0;width:1280px;height:1274px;transform:scale(.93125,.9419);transform-origin:0 0}
.abs{position:absolute}

.site-header{left:150px;top:0;width:960px;height:105px;background:var(--charcoal);border-radius:0 0 16px 16px;box-shadow:0 2px 4px rgba(0,0,0,.3)}
.brand{left:30px;top:30px;display:flex;align-items:center;gap:12px}
.brand-mark{width:56px;height:56px;background:var(--red)}
.brand-name{font-size:32px;color:var(--white);font-weight:400}
.call{right:28px;top:66px;color:var(--white);font-size:16px;font-weight:700;white-space:nowrap}
.call strong{font-size:24px;font-weight:400;margin-left:4px}

.main-nav{left:172px;top:122px;width:918px;height:31px;display:flex;align-items:center;justify-content:space-between;list-style:none}
.main-nav li{font-size:14px;font-weight:700;color:var(--ink);white-space:nowrap}
.main-nav li.current{background:var(--charcoal);color:var(--white);border-radius:16px;width:115px;height:31px;line-height:31px;text-align:center;box-shadow:0 1px 3px rgba(0,0,0,.4)}
.nav-rule{left:150px;top:161px;width:960px;height:1px;background:var(--line)}

.hero{left:150px;top:162px;width:960px;height:361px;background:linear-gradient(160deg,#f8f8f8 0%,#e2e2e2 60%,#d0d0d0 100%);overflow:hidden}
.hero-photo{right:0;top:0;width:450px;height:361px;background:radial-gradient(ellipse at 70% 35%,#f2e4cf 0%,#d9d9d9 45%,#2a2a2a 100%);opacity:.9}
.hero h1{left:30px;top:76px;font-size:44px;font-weight:400;color:var(--red);white-space:nowrap}
.hero p{left:31px;top:146px;width:400px;font-size:17px;line-height:22px;color:var(--ink)}
.btn{display:inline-block;background:linear-gradient(#d42a2d,#a80f12);color:var(--white);font-weight:700;font-size:13px;border-radius:16px;text-align:center;box-shadow:0 1px 2px rgba(0,0,0,.35);white-space:nowrap}
.hero .btn{left:30px;top:230px;width:121px;height:30px;line-height:30px}
.slider-bar{left:150px;top:523px;width:961px;height:23px;background:linear-gradient(#e8e8e8,#cfcfcf);border:1px solid #bbb}
.dots{left:471px;top:6px;display:flex;gap:5px}
.dots span{width:11px;height:11px;border-radius:50%;background:#111}
.dots span:first-child{background:var(--red)}

.feature{top:572px;width:311px;height:171px;border:1px solid #e4e4e4;border-radius:4px;padding:3px}
.feature-inner{position:relative;width:100%;height:100%;border:1px solid #bdbdbd;border-radius:4px;background:linear-gradient(#fff,#dcdcdc);padding:8px 16px}
.feature h2{font-size:23px;font-weight:400;color:var(--ink);margin-bottom:4px;white-space:nowrap}
.feature p{font-size:10.5px;line-height:13px;color:#333}
.feature p.tag{margin-top:14px;font-weight:700;letter-spacing:.5px}
.feature .btn{position:absolute;left:23px;bottom:-14px;width:100px;height:28px;line-height:28px}
.badges{display:flex;gap:22px;margin-top:16px;align-items:center}
.badge{height:34px;background:#cfcfcf;border-radius:4px}

.welcome{left:150px;top:800px;width:595px}
.welcome h2{font-size:30px;font-weight:400;color:var(--ink);margin-bottom:10px}
.welcome p{font-size:12px;line-height:14.5px;color:#333;margin-bottom:14px}
.divider{left:784px;top:798px;width:1px;height:308px;background:var(--line)}

.sidebar h3{font-size:24px;font-weight:400;color:var(--ink);white-space:nowrap}
.promo{left:819px;top:845px;width:274px;height:176px;border:1px solid #bbb;border-radius:12px;background:linear-gradient(#fff,#e2e2e2);padding:13px 11px}
.promo p{width:132px;font-size:11px;line-height:13.3px;color:#333}
.promo a{position:absolute;left:11px;top:145px;font-size:12px;font-weight:700;color:var(--red-dark);text-decoration:none}
.promo-photo{left:147px;top:14px;width:122px;height:145px;border-radius:6px;background:linear-gradient(135deg,#333 0%,#6a5a4a 45%,#e06a2a 100%)}
.newsletter-title{left:818px;top:1052px;font-size:18px!important}
.email{left:819px;top:1082px;width:275px;height:27px;border:1px solid #ccc;font-size:11px;color:#999;padding:6px 8px;letter-spacing:.5px}
.subscribe{left:1013px;top:1115px;width:80px;height:28px;line-height:28px}

.site-footer{left:150px;top:1203px;width:960px;height:71px;border-radius:14px 14px 0 0;background:linear-gradient(#c81a1d,#a10d10);box-shadow:0 -1px 4px rgba(0,0,0,.3);color:var(--white);font-size:12.5px;font-weight:700;text-align:center;padding-top:30px;letter-spacing:.3px}
</style>
</head>
<body>
<div class="stage">
  <header class="site-header abs">
    <div class="brand abs"><span class="brand-mark"></span><span class="brand-name">Norva eX</span></div>
    <div class="call abs">Call Us Now: <strong>+61 8 5550 1234</strong></div>
  </header>

  <ul class="main-nav abs">
    <li class="current">Home</li>
    <li>About Us</li>
    <li>Facilities</li>
    <li>Business Continuity</li>
    <li>Services</li>
    <li>Partners</li>
    <li>Webmail</li>
    <li>Contact Us</li>
  </ul>
  <div class="nav-rule abs"></div>

  <section class="hero abs">
    <div class="hero-photo abs" role="img" aria-label="Photo of a professional working on a laptop"></div>
    <h1 class="abs">Safe, Secure, Reliable</h1>
    <p class="abs">Perth's Safe, Secure &amp; Reliable Data Centre" Talk to us about designing a solution to meet your needs.</p>
    <span class="btn abs">Read More</span>
  </section>
  <div class="slider-bar abs"><div class="dots abs"><span></span><span></span><span></span></div></div>

  <article class="feature abs" style="left:150px">
    <div class="feature-inner">
      <h2>Business Continuity</h2>
      <p>No matter how safe and secure you feel right now, the stability of your entire organisation could be under serious threat! Whether a natural disaster such as fire or flood, or man made issue such as arson or theft, these disasters could cause untold damage to your IT infrastructure.</p>
      <span class="btn">Read More</span>
    </div>
  </article>
  <article class="feature abs" style="left:476px">
    <div class="feature-inner">
      <h2>Norva eX Services</h2>
      <p>Norva eX currently offers colocation services with unsurpassed reliability and speed to hundreds of Australian based and international clients.</p>
      <p class="tag">Innovative IT Solutions...</p>
      <span class="btn">Read More</span>
    </div>
  </article>
  <article class="feature abs" style="left:802px">
    <div class="feature-inner">
      <h2>Partners</h2>
      <p>Norva eX is proud to partner with many of Australia's leading companies.</p>
      <div class="badges">
        <span class="badge" style="width:80px"></span>
        <span class="badge" style="width:48px;border-radius:50%;height:44px"></span>
        <span class="badge" style="width:98px"></span>
      </div>
      <span class="btn">Read More</span>
    </div>
  </article>

  <section class="welcome abs">
    <h2>Welcome to Norva eX</h2>
    <p>A world class data centre in the safest place on Earth.</p>
    <p>With a centrally located data centre in the heart of the Perth CBD Norva eX is excellently positioned to assist with your critical IT requirements.</p>
    <p>The CBD facility features overlapping power grids, redundant power supplies and comprehensively maintained infrastructure,&nbsp; providing excellent levels of protection for your critical IT equipment. The State's newest and most technologically advanced data centre is also now open in Belmont, a convenient 5.5 km's from the CBD providing a perfect location for either production sites, or DR infrastructure.</p>
    <p>From Government departments to large corporations to SME's, Norva eX is the ideal company to assist with your colocation requirements. With warm racks already provisioned, you can begin using the data centre almost immediately.</p>
    <p>Call us today to see how we can help meet your needs.</p>
  </section>
  <div class="divider abs"></div>

  <aside class="sidebar">
    <h3 class="abs" style="left:818px;top:804px">Current Promo</h3>
    <div class="promo abs">
      <p>Lorem Ipsum is simply dummy text of the printing and typesetting industry. Lorem Ipsum has been the industry's standard dummy text ever since the 1500s.</p>
      <a href="#">Read More</a>
      <div class="promo-photo abs" role="img" aria-label="Photo of server rack equipment"></div>
    </div>
    <h3 class="newsletter-title abs">Subscribe for Newsletter</h3>
    <div class="email abs">Email Address...</div>
    <span class="btn subscribe abs">Subscribe</span>
  </aside>

  <footer class="site-footer abs">Copyright © 2010 norvalex.example. All Right Reserved.</footer>
</div>
</body>
</html>
```